Advertising flyer for proofreading business.

Hello everyone,

I need an advertising flyer for a new proofreading company in Australia.

I would like your design in be in two sizes:
- A4 (to be posted on noticeboards),
- A6 (to be printed in larger quantity to give away)
(please see the size specification file attached).

The text file is attached (Ad Text) and it contains lots of information. Please feel free to include your choice of text from the text file, but please include Poster title, and highlight 'ESL' and students discounts.

I understand that it is impossible to include the same amount of information on A6 and A4, so please feel free to chose what fits on each of them, but please keep the design similar.

I have attached our company logo, but feel free to adjust it to the poster design (feel free to change the color as well). The original logo file contains circle around it, please feel free to remove it and include only the typeset as it can be seen here: http://www.lexmarka.com.au/.

Flyers will be printed, so please see the specification file for details.

I will do my best to respond to feedback as soon as possible.

I appreciate your participation, time and help,
Best wishes,
Bartosz

Target Market(s)

Students, authors

Industry/Entity Type

Business

Colors

Designer to choose colors to be used in the design.

Requirements
Must have
• It would be good if poster is easy to spot on busy noticeboards and attract attention.
• Please keep the poster in the positive/optimistic mood, and so that it focuses on students, maybe photos of graduates(?).
• Poster title,
• Please include the list of proof-read documents as they are described in the attached text file (Ad Text).
• Please highlight students discounts and ESL.
Nice to have
• I would like to leave the creative freedom to all designers so at this point I have not adjusted the Look and Feel sliders. Please feel free to offer your own take on this.
• It would be nice if most of the text could be fit to the poster.

```html
<!DOCTYPE html>
<html lang="en">
<head>
<meta charset="utf-8">
<title>Prosewell – Professional English Language Proofreading</title>
<link rel="stylesheet" href="https://fonts.googleapis.com/css2?family=Roboto:wght@300;500&family=Roboto+Condensed:wght@400;700&family=Marcellus&family=Alegreya:wght@400&family=Open+Sans:wght@700&display=swap">
<style>
  :root {
    --teal: #66c2b6;
    --teal-text: #5bbfb3;
    --teal-dark: #3e9a90;
    --ink: #3a3a3a;
    --dark: #111111;
    --white: #ffffff;
  }
  * { margin: 0; padding: 0; box-sizing: border-box; }
  html, body { width: 873px; height: 1200px; overflow: hidden; background: var(--white); }
  .flyer { position: relative; width: 873px; height: 1200px; background: var(--white); overflow: hidden; }

  .title {
    position: absolute; left: 40px; top: 48px;
    font-family: "Roboto", sans-serif; font-weight: 300;
    font-size: 55px; line-height: 58px; color: var(--teal-text);
    letter-spacing: 0.5px;
  }

  .student-photo {
    position: absolute; left: 0; top: 295px; width: 503px; height: 378px;
    background: linear-gradient(180deg, #a9c6a0 0%, #7d8f6a 35%, #5b6f8e 60%, #c9cbc7 100%);
  }

  .circle-clip { position: absolute; left: 0; top: 0; width: 503px; height: 1200px; overflow: hidden; }
  .circle-ring {
    position: absolute; left: 381px; top: 242px; width: 496px; height: 496px;
    border-radius: 50%; background: var(--white);
  }
  .circle-fill {
    position: absolute; left: 389px; top: 250px; width: 480px; height: 480px;
    border-radius: 50%; background: var(--teal);
  }

  .side-panel { position: absolute; left: 503px; top: 0; width: 370px; height: 1200px; background: var(--teal); }

  .esl-heading {
    position: absolute; left: 503px; width: 370px; top: 42px;
    text-align: center; font-family: "Roboto", sans-serif; font-weight: 300;
    font-size: 51px; line-height: 57px; color: var(--white);
  }

  .brand {
    position: absolute; left: 470px; width: 400px; top: 500px;
    text-align: center; font-family: "Roboto", sans-serif; font-weight: 300;
    font-size: 74px; line-height: 80px; color: var(--white);
  }

  .credential {
    position: absolute; left: 503px; width: 370px; top: 667px;
    text-align: center; font-family: "Open Sans", sans-serif; font-weight: 700;
    font-size: 18.5px; line-height: 28px; color: var(--white);
  }

  .testimonial-label {
    position: absolute; left: 503px; width: 370px; top: 795px;
    text-align: center; font-family: "Marcellus", serif; font-weight: 400; font-size: 21px; color: var(--dark);
  }
  .testimonial-quote {
    position: absolute; left: 520px; width: 323px; top: 838px;
    font-family: "Alegreya", serif; font-size: 16.5px; line-height: 24px;
    color: var(--white); text-align: justify; text-align-last: center;
  }
  .testimonial-name {
    position: absolute; left: 503px; width: 370px; top: 946px;
    text-align: center; font-family: "Alegreya", serif; font-size: 21px; color: var(--white);
  }
  .testimonial-role {
    position: absolute; left: 503px; width: 370px; top: 973px;
    text-align: center; font-family: "Alegreya", serif; font-size: 16px; color: var(--white);
  }

  .contact-call {
    position: absolute; left: 503px; width: 370px; top: 1036px;
    text-align: center; font-family: "Roboto Condensed", sans-serif; font-weight: 400;
    font-size: 26px; line-height: 27px; color: var(--dark);
  }
  .contact-phone {
    position: absolute; left: 503px; width: 370px; top: 1093px;
    text-align: center; font-family: "Roboto Condensed", sans-serif; font-weight: 700;
    font-size: 40px; color: var(--white);
  }
  .contact-email {
    position: absolute; left: 503px; width: 370px; top: 1141px;
    text-align: center; font-family: "Roboto Condensed", sans-serif; font-weight: 700;
    font-size: 24px; color: var(--dark);
  }

  .documents-banner {
    position: absolute; left: 0; top: 656px; width: 323px; height: 36px;
    background: var(--teal-dark);
    clip-path: polygon(0 0, 100% 0, 89% 100%, 0 100%);
  }
  .documents-banner span {
    position: absolute; left: 38px; top: 5px;
    font-family: "Marcellus", serif; font-size: 21px; color: var(--white);
  }

  .document-list {
    position: absolute; left: 41px; top: 706px; list-style: none;
    font-family: "Marcellus", serif; font-size: 14.5px; line-height: 21.6px; color: var(--ink);
  }
  .document-list li { display: flex; align-items: center; gap: 5px; }
  .document-list svg { width: 11px; height: 11px; flex: none; }

  .price-heading {
    position: absolute; left: 40px; top: 956px;
    font-family: "Marcellus", serif; font-size: 21px; color: var(--teal-dark);
  }
  .price-list {
    position: absolute; left: 41px; top: 995px; width: 345px; list-style: none;
    font-family: "Alegreya", serif; font-size: 13.5px; line-height: 16.5px; color: var(--ink);
  }
  .price-list li { position: relative; padding-left: 20px; margin-bottom: 7px; }
  .price-list li::before {
    content: ""; position: absolute; left: 2px; top: 3px; width: 11px; height: 11px;
    border-radius: 50%; background: radial-gradient(circle at 35% 35%, #8fdacf, var(--teal-dark));
  }

  .website {
    position: absolute; left: 40px; top: 1140px;
    font-family: "Roboto Condensed", sans-serif; font-weight: 700;
    font-size: 23px; letter-spacing: 2.4px; color: var(--teal-dark);
  }
</style>
</head>
<body>
<div class="flyer">
  <h1 class="title">PROFESSIONAL<br>ENGLISH<br>LANGUAGE<br>PROOFREADING</h1>

  <div class="student-photo" role="img" aria-label="Photo of five smiling students walking together on a sunny campus, carrying books and laptops"></div>

  <div class="circle-clip">
    <div class="circle-ring"></div>
    <div class="circle-fill"></div>
  </div>

  <div class="side-panel"></div>

  <h2 class="esl-heading">Help with<br>English as a<br>Second<br>Language<br>(ESL)</h2>

  <div class="brand">Prosewell</div>

  <p class="credential">Proofreading by a native<br>English speaker with an<br>Honours degree in English.</p>

  <h3 class="testimonial-label">Testimonial</h3>
  <p class="testimonial-quote">Hannah understood our requirements quickly and has been fantastic at delivering quality work, on time and within an agreed budget. It’s a pleasure to work with her.</p>
  <p class="testimonial-name">CAROL WESTON</p>
  <p class="testimonial-role">Operations Manager, Northbay Logistics</p>

  <p class="contact-call">CONTACT US FOR AN<br>OBLIGATION FREE QUOTE</p>
  <p class="contact-phone">0400 512 377</p>
  <p class="contact-email">proofing@prosewell.com.au</p>

  <div class="documents-banner"><span>Documents include:</span></div>

  <ul class="document-list">
    <li><svg viewBox="0 0 12 12"><path d="M1 6.5 L4.5 10 L11 1.5" fill="none" stroke="#3e9a90" stroke-width="2"/></svg>Essays and assignments</li>
    <li><svg viewBox="0 0 12 12"><path d="M1 6.5 L4.5 10 L11 1.5" fill="none" stroke="#3e9a90" stroke-width="2"/></svg>Theses</li>
    <li><svg viewBox="0 0 12 12"><path d="M1 6.5 L4.5 10 L11 1.5" fill="none" stroke="#3e9a90" stroke-width="2"/></svg>Resumes</li>
    <li><svg viewBox="0 0 12 12"><path d="M1 6.5 L4.5 10 L11 1.5" fill="none" stroke="#3e9a90" stroke-width="2"/></svg>Business correspondence</li>
    <li><svg viewBox="0 0 12 12"><path d="M1 6.5 L4.5 10 L11 1.5" fill="none" stroke="#3e9a90" stroke-width="2"/></svg>Training manuals</li>
    <li><svg viewBox="0 0 12 12"><path d="M1 6.5 L4.5 10 L11 1.5" fill="none" stroke="#3e9a90" stroke-width="2"/></svg>Newsletters</li>
    <li><svg viewBox="0 0 12 12"><path d="M1 6.5 L4.5 10 L11 1.5" fill="none" stroke="#3e9a90" stroke-width="2"/></svg>Advertising copy</li>
    <li><svg viewBox="0 0 12 12"><path d="M1 6.5 L4.5 10 L11 1.5" fill="none" stroke="#3e9a90" stroke-width="2"/></svg>Brochures, catalogues and media releases</li>
    <li><svg viewBox="0 0 12 12"><path d="M1 6.5 L4.5 10 L11 1.5" fill="none" stroke="#3e9a90" stroke-width="2"/></svg>Websites</li>
    <li><svg viewBox="0 0 12 12"><path d="M1 6.5 L4.5 10 L11 1.5" fill="none" stroke="#3e9a90" stroke-width="2"/></svg>Presentations and speeches</li>
    <li><svg viewBox="0 0 12 12"><path d="M1 6.5 L4.5 10 L11 1.5" fill="none" stroke="#3e9a90" stroke-width="2"/></svg>Novels and short stories</li>
  </ul>

  <h3 class="price-heading">PRICE GUIDE:</h3>
  <ul class="price-list">
    <li>Discounts for not-for-profit organisations.</li>
    <li>Great student discount rate: $25 per hour (roughly 1000 words - 4 pages - of well-written text).</li>
    <li>Package deals on documents over 50,000 words.</li>
    <li>Fast, negotiable time-frames (same day service available by special arrangement).</li>
  </ul>

  <p class="website">www.prosewell.com.au</p>
</div>
</body>
</html>
```